Lantern Hearthworks Business Cards

Looking to create simple business cards that highlight our unique three sided triangle fire pit design with the colors and font of our logo, listed below.

Colors

Designer to choose colors to be used in the design.

Requirements
Must have
• Looking for something simple that includes a picture of our fire pit with name, website (lanternhearthworks.com), phone number and email. Want to keep the color mostly orange and black.
• Font is gotham(medium) and orange color code is #ee6e22

```html
<!DOCTYPE html>
<html lang="en">
<head>
<meta charset="utf-8">
<title>Lantern Hearthworks Business Cards</title>
<link rel="stylesheet" href="https://fonts.googleapis.com/css2?family=Montserrat:wght@500;600&display=swap">
<style>
  :root {
    --orange: #ee6e22;
    --grey: #6b6b6d;
    --rule: #cfcfcf;
    --ink: #2b2b2b;
    --stage: #3b3b3d;
    --card: #ffffff;
  }
  * { box-sizing: border-box; margin: 0; padding: 0; }
  html, body { width: 1200px; height: 866px; overflow: hidden; background: var(--stage); }
  body { font-family: "Montserrat", Arial, sans-serif; position: relative; }

  .card {
    position: absolute;
    left: 285px;
    width: 630px;
    height: 360px;
    border-radius: 4px;
    overflow: hidden;
    box-shadow: 0 10px 30px rgba(0,0,0,.45);
  }
  .card--front { top: 53px; background: var(--card); }
  .card--back  { top: 453px; }

  .holder-name {
    position: absolute; left: 40px; top: 138px;
    font-weight: 600; font-size: 21px; letter-spacing: 1px;
    text-transform: uppercase; color: var(--orange);
  }
  .contact { position: absolute; left: 40px; top: 178px; list-style: none; }
  .contact li {
    display: flex; align-items: center; gap: 8px;
    font-weight: 500; font-size: 14px; color: var(--ink); line-height: 22px;
  }
  .contact svg { width: 15px; height: 15px; flex: none; }

  .divider-v { position: absolute; left: 330px; top: 92px; width: 1px; height: 110px; background: var(--rule); }
  .divider-h { position: absolute; left: 232px; top: 200px; width: 360px; height: 1px; background: var(--rule); }

  .brand-mark {
    position: absolute; left: 352px; top: 104px;
    display: flex; align-items: center; gap: 12px;
  }
  .brand-mark .dot { width: 16px; height: 16px; border-radius: 50%; background: var(--orange); flex: none; }
  .brand-name {
    font-weight: 500; font-size: 24px; line-height: 30px;
    letter-spacing: 4px; text-transform: uppercase; color: var(--orange);
  }

  .website {
    position: absolute; right: 40px; top: 288px;
    font-weight: 500; font-size: 14px; color: var(--ink);
  }
  .website span { color: var(--orange); }

  .card-bands { position: absolute; left: 0; bottom: 0; width: 630px; height: 30px; }

  .fire-pit-photo {
    width: 100%; height: 100%;
    background:
      radial-gradient(ellipse 120px 70px at 52% 48%, rgba(238,110,34,.9), rgba(238,110,34,0) 70%),
      radial-gradient(ellipse 190px 130px at 50% 50%, #1c1c1c, rgba(28,28,28,0) 75%),
      linear-gradient(135deg, #4a4a4a, #2e2e2e);
  }
</style>
</head>
<body>

<section class="card card--front" aria-label="Business card front">
  <p class="holder-name">Marcus Hale</p>
  <ul class="contact">
    <li>
      <svg viewBox="0 0 16 16" aria-hidden="true"><rect x="1" y="1" width="14" height="14" rx="2" fill="none" stroke="#ee6e22" stroke-width="1.5"/><path d="M5 4c-1 1-1 3 1 5s4 2.5 5 1.5l-1.4-1.6-1.2.8c-.8-.3-2-1.5-2.3-2.3l.8-1.2z" fill="#ee6e22"/></svg>
      044-210 387 654
    </li>
    <li>
      <svg viewBox="0 0 16 16" aria-hidden="true"><rect x="1" y="3" width="14" height="10" fill="#ee6e22"/><path d="M1 3l7 6 7-6" fill="none" stroke="#fff" stroke-width="1.3"/></svg>
      hello@hearthmail.com
    </li>
  </ul>

  <div class="divider-v"></div>
  <div class="divider-h"></div>

  <div class="brand-mark">
    <span class="dot"></span>
    <p class="brand-name">Lantern<br>Hearthworks</p>
  </div>

  <p class="website">www.<span>lanternhearthworks</span>.com</p>

  <svg class="card-bands" viewBox="0 0 630 30" preserveAspectRatio="none" aria-hidden="true">
    <polygon points="0,16 340,16 340,30 0,30" fill="#ee6e22"/>
    <polygon points="340,30 358,6 630,6 630,30" fill="#6b6b6d"/>
  </svg>
</section>

<section class="card card--back" aria-label="Business card back">
  <div class="fire-pit-photo" role="img" aria-label="Photograph of the three-sided triangular steel fire pit burning on dark gravel"></div>
</section>

</body>
</html>
```